4 x Designs Required

Hi There,
I require 4 x different designs to be made for 4 new brands of mine however they can be quite interchangeable. HR Plinkr and Marketing Plinkr can be similar just with a difference in colour. The same goes for the Bulletin brands. This means there are ultimately two designs that need perfecting.

There must be a click here CTA on the banner somewhere. :-)

I require the banners in 728x90 format and 960x90 please.

Please use strap lines on the banners such as:
Essential Whitepapers for HR Professionals
Essential Whitepapers for Marketing Professionals
Your No.1 Whitepaper Resource

The brand names:
HR Plinkr
Marketing Plinkr
HR Dispatchly
Marketing Dispatchly

Examples attached.

```html
<!DOCTYPE html>
<html lang="en">
<head>
<meta charset="utf-8">
<title>Marketing Dispatchly – Leaderboard Banner</title>
<link rel="stylesheet" href="https://fonts.googleapis.com/css2?family=PT+Sans:wght@400;700&display=swap">
<style>
  :root {
    --bg-left: #cfcbb7;
    --bg-khaki: #b5ae88;
    --bg-mid: #8b907a;
    --bg-sage: #5d7a5f;
    --bg-right: #2c4621;
    --ink: #0d0d0d;
    --paper: #ffffff;
  }

  * { margin: 0; padding: 0; box-sizing: border-box; }

  html, body {
    width: 1200px;
    height: 112px;
    overflow: hidden;
    background: var(--paper);
  }

  .banner {
    position: relative;
    width: 1200px;
    height: 112px;
    overflow: hidden;
    background: linear-gradient(90deg, var(--bg-left) 0%, #bdb9a2 22%, var(--bg-mid) 50%, #56704d 76%, var(--bg-right) 100%);
  }

  .banner__texture {
    position: absolute;
    inset: 0;
    background:
      linear-gradient(180deg, rgba(181, 174, 136, 0.35) 0%, rgba(181, 174, 136, 0) 60%),
      linear-gradient(0deg, rgba(93, 122, 95, 0.3) 0%, rgba(93, 122, 95, 0) 55%);
  }

  .brand-name {
    position: absolute;
    left: 27px;
    top: 36px;
    font-family: "PT Sans", "Arial", sans-serif;
    font-weight: 700;
    font-size: 36px;
    line-height: 1;
    color: var(--ink);
    white-space: nowrap;
  }

  .strapline {
    position: absolute;
    left: 455px;
    top: 43px;
    font-family: "PT Sans", "Arial", sans-serif;
    font-weight: 400;
    font-size: 23px;
    line-height: 1;
    color: var(--paper);
    white-space: nowrap;
  }

  .cta {
    position: absolute;
    left: 1075px;
    top: 40px;
    width: 96px;
    height: 35px;
    border-radius: 8px;
    background: var(--ink);
    color: var(--paper);
    font-family: "PT Sans", "Arial", sans-serif;
    font-weight: 700;
    font-size: 18px;
    line-height: 35px;
    text-align: center;
    text-decoration: none;
  }
</style>
</head>
<body>
  <div class="banner">
    <div class="banner__texture" role="img" aria-label="Soft khaki and sage background texture"></div>
    <div class="brand-name">Marketing Dispatchly</div>
    <p class="strapline">Essential Whitepapers for HR Professionals</p>
    <a class="cta" href="#">SIGN UP</a>
  </div>
</body>
</html>
```